Broschüren-Design für Verkauf von Produkten aus Holz
Die Kommunikation mit dem Designer ROL war durchweg einwandfrei! Änderungswünsche wurden in kürzester Zeit umgesetzt. Jederzeit gerne wieder!
Zielgruppe
Seit über 60 Jahren fertigt die Feldner GmbH & Co. KG Produkte aus Holz.
Zielgruppe sind Küchenstudios .
Aufgabenstellung
Feldner-Küchenstudio Broschüre/Katalog
Aufgabenstellung:
Es soll ein Katalog (PDF zum Blättern & Druckversion) erstellt werden in 3 Sprachen speziell für Küchenstudios, aufgeteilt in 6 Rubriken (je Rubrik 2-6 Seiten) + ansprechendes Deckblatt mit unserem Logo und einem Slogan aus dem sinngemäß hervorgeht, dass es sich bei unseren Produkten um maßangefertigte Unikate aus der Natur handelt. Relativ wenig Text Gesamtumfang ca. 24-30 Seiten.
Rubriken:
- Holzarten kgz + durchgehend
- Thekenplatte & Thekenaufsätze
- Küchenarbeitsplatten
- Massivholzfronten
- Tische/Tischplatten
- Schneidbretter/Hackklotz
- Magnetmesserblöcke
Ziel:
Es soll vermittelt werden:
- Massivholz passt nahezu zu jeder Küche
- In Küchen Akzente mit Massivholzkomponenten zu setzen und diese damit aufzuwerten.
- Auf Wunschmaß individuell in Deutschland gefertigt
- Erweiterungen & Austausch auf vorhandenen Küchen möglich
Unsere Grobvorstellung:
1. Innenseite: Wir über uns... mit Bildern der Ansprechpartner sowie Luftbild Firma
2. Seite: Inhaltsverzeichnis mit Seitenzahl der erhältlichen Produkte (Rubriken)
Ab Seite 3: Bilder der einzelnen Rubriken mit KLEINEN Textfelder, diese werden nachträglich von uns bearbeitet/erstellt
Letzte Seite: Informationen über Lieferung & Lieferzeiten
Rückseite: Basierend auf Deckblatt und unserem Logo (nicht all zu groß) mit Adress & Kontaktdaten
Die Bilder für die einzelnen Rubriken werden von uns gestellt, ergänzend sollen passende Bilder aus verschiedenen Quellen zu den verschiedenen Rubriken hinzugezogen werden, die mit entsprechender Genehmigung verwendet werden dürfen.
Ansonsten steht der Gestaltung und dem Design keine weiteren Vorgaben im Weg.

```html
<!DOCTYPE html>
<html lang="de">
<head>
<meta charset="utf-8">
<title>Feldner – Wir über uns</title>
<link href="https://fonts.googleapis.com/css2?family=Inter:wght@300;400;600&display=swap" rel="stylesheet">
<style>
  :root {
    --stage: #d5d3da;
    --paper: #ffffff;
    --sand: #d1ccc8;
    --portrait: #96979a;
    --ink-strong: #3b3b3b;
    --ink-body: #707070;
    --photo-green: #6f9a4a;
    --photo-roof: #a9adb2;
  }
  * { margin: 0; padding: 0; box-sizing: border-box; }
  html, body { width: 1200px; height: 959px; overflow: hidden; }
  body {
    position: relative;
    background: var(--stage);
    font-family: "Inter", Helvetica, Arial, sans-serif;
    color: var(--ink-body);
  }
  .spread {
    position: absolute; left: 95px; top: 107px;
    width: 1008px; height: 712px;
    background: var(--paper);
  }
  .sand-panel {
    position: absolute; left: 246px; top: 0;
    width: 444px; height: 712px;
    background: var(--sand);
  }
  .aerial-photo {
    position: absolute; left: 47px; top: 102px;
    width: 262px; height: 182px;
    background: linear-gradient(135deg, var(--photo-green) 0%, var(--photo-roof) 45%, #c9cbcd 60%, var(--photo-green) 100%);
  }
  .slogan {
    position: absolute; left: 76px; top: 332px;
    font-weight: 300; font-size: 20px; line-height: 29px;
    color: var(--ink-strong); letter-spacing: -0.4px;
  }
  .section-title {
    position: absolute;
    font-weight: 600; font-size: 12.5px; letter-spacing: 0.1px;
    color: var(--ink-strong);
  }
  .copy {
    position: absolute;
    font-weight: 300; font-size: 7.4px; line-height: 19.5px;
    color: var(--ink-body);
  }
  .copy span { display: block; text-align: justify; text-align-last: justify; white-space: nowrap; }
  .copy span.end { text-align-last: left; }
  .copy span.gap { height: 19.5px; }
  .portrait {
    position: absolute; left: 551px;
    width: 89px; height: 110px;
    background: var(--portrait);
  }
  .person {
    position: absolute; left: 551px;
    font-size: 7.4px; line-height: 10px;
  }
  .person .role { font-weight: 300; color: var(--ink-body); }
  .person .name { font-weight: 400; color: var(--ink-strong); font-size: 8px; }
</style>
</head>
<body>
<main class="spread">
  <div class="sand-panel"></div>

  <div class="aerial-photo" role="img" aria-label="Luftbild des Firmengeländes mit Hallen und Grünflächen"></div>

  <h2 class="slogan">Details sind der<br>Schlüssel zur<br>Perfektion</h2>

  <h1 class="section-title" style="left:47px; top:480px;">IMPRESSUM. WIR ÜBER UNS</h1>
  <p class="copy" style="left:47px; top:505px; width:186px;">
    <span>Seit fast 60 Jahren fertigt die Feldner GmbH &amp; Co. KG</span>
    <span>Produkte aus Holz. Teils handwerklich, teils industriell.</span>
    <span>Das Feldner-Team, bestehend aus über 25 qualifizierten</span>
    <span>Mitarbeitern mit langjähriger Erfahrung in der Holz-</span>
    <span>ver- u. bearbeitung sowie der Oberflächenbehand-</span>
    <span>lung, sorgt dafür, dass unsere Kunden Ihre Produkte in</span>
    <span class="end">hochwertiger Qualität und zuverlässig erhalten.</span>
  </p>

  <p class="copy" style="left:262px; top:505px; width:186px;">
    <span>Teil unseres Portfolios ist der Handel und die Bearbei-</span>
    <span>tung von Massivholzplatten. Leimholzplatten aus ed-</span>
    <span>len Laubhölzern, in Standard- oder Meisterqualität,</span>
    <span>werden beispielsweise zur Herstellung von Tischplat-</span>
    <span>ten, Treppenstufen, Podestplatten, Treppenwangen,</span>
    <span>Küchenarbeitsplatten, Büroarbeitsplatten, Werkbank-</span>
    <span class="end">platten, Türrahmen, Fensterbänke u.a.</span>
  </p>

  <div class="portrait" style="top:125px;" role="img" aria-label="Porträtfoto Geschäftsführer"></div>
  <p class="person" style="top:246px;"><span class="role">GESCHÄFTSFÜHRER</span><br><span class="name">Vorname Familienname</span></p>

  <div class="portrait" style="top:295px;" role="img" aria-label="Porträtfoto Geschäftsführer"></div>
  <p class="person" style="top:418px;"><span class="role">GESCHÄFTSFÜHRER</span><br><span class="name">Vorname Familienname</span></p>

  <div class="portrait" style="top:477px;" role="img" aria-label="Porträtfoto Geschäftsführer"></div>
  <p class="person" style="top:599px;"><span class="role">GESCHÄFTSFÜHRER</span><br><span class="name">Vorname Familienname</span></p>

  <h1 class="section-title" style="left:719px; top:124px;">WIR ÜBER UNS</h1>
  <p class="copy" style="left:719px; top:145px; width:229px;">
    <span>Teil unseres Portfolios ist der Handel und die Bearbeitung von Mas-</span>
    <span>sivholzplatten. Leimholzplatten (auch Vollholz- oder Einschicht-</span>
    <span>platten genannt) aus edlen Laubhölzern, in Standardqualität oder</span>
    <span>Meisterqualität, werden zur Herstellung von Tischplatten, Treppen-</span>
    <span>stufen, Podestplatten, Treppenwangen, Küchenarbeitsplatten,</span>
    <span>Büroarbeitsplatten, Werkbankplatten, Türrahmen, Fensterbänken</span>
    <span>und Möbelteilen, Möbel sowie von Teilen für den Innenausbau ver-</span>
    <span>wendet. Dies individuell nach Ihren Vorgaben oder Wünschen oder</span>
    <span class="end">als Standardprodukte.</span>
    <span class="gap"></span>
    <span>Was bieten wir noch? Tische und Bänke aus Massivholz (Vollholz),</span>
    <span>schöne Tischgestelle und Bankgestelle aus Edelstahl, Holz, Alumi-</span>
    <span>niumin oder Stahl pulverbeschichtet oder verchromt. Tischplatten</span>
    <span>und Tischgestelle können auch separat geliefert werden. Wir sind</span>
    <span>Ihr Ansprechpartner für Tische und Tischplatten für die Gastrono-</span>
    <span>mie. Neu im Sortiment: Sitzmöbel - Stühle in modernem Design in</span>
    <span>Lederoptik oder Corvana Samt. Außerdem sind wir Systemlieferant</span>
    <span>für Handläufe bzw Geländer-Stangen aus Holz und Edelstahl mit</span>
    <span>einem umfassenden Zubehör- und Leistungsspektrum - auch Bal-</span>
    <span>lettstangen. Diese können Sie direkt online in unserem handlauf-</span>
    <span>feldner.shop bestellen. Passend hierzu bieten wir Treppenstufen aus</span>
    <span>Massivholz für alle Treppenarten. Ergänzt wird das Massivholzsor-</span>
    <span>timent durch ausgewählte Zubehörteile speziell für den Tischbau,</span>
    <span>Küchenbau sowie für den Möbel- und Innenausbau. Ebenfalls sind</span>
    <span>wir Hersteller von Magnet-Messerblöcken. Feldner-Design fertigt</span>
  </p>
</main>
</body>
</html>
```